Exciting new female owned mobile Aesthetics company preparing for our first tradeshows!

We are a simple, elegant and fresh female owned concierge/mobile aesthetics company, catering to both men and women ages 30-60. We are looking for booth decoration ideas. We are a service based company that is not selling products, so we need ideas for banners and tabletop designs. We would like the design to match our logo and website colors. Website is at www(dot)fernquill(dot)com.

Target Market(s)

30-60 year old men and women, but mostly women

Industry/Entity Type

beauty and aesthetics

Font styles to use
Sans Serif
Script

Requirements
Must have
• Retractable Banner designs (33inch x 80inch) All designs need to match colors and design of logo and website at fernquill(dot)com

```html
<!DOCTYPE html>
<html lang="en">
<head>
<meta charset="utf-8">
<title>Fernquill Concierge Aesthetics – Tabletop Cover</title>
<link rel="stylesheet" href="https://fonts.googleapis.com/css2?family=Cinzel:wght@400;500&display=swap">
<style>
  :root {
    --pink: #e8338f;
    --coral: #f06a63;
    --orange: #f7941d;
    --outline: #cfcfcf;
    --paper: #ffffff;
  }
  html, body {
    margin: 0;
    padding: 0;
    width: 1200px;
    height: 1200px;
    overflow: hidden;
    background: var(--paper);
  }
  .canvas {
    position: relative;
    width: 1200px;
    height: 1200px;
  }
  .table-cover {
    position: absolute;
    left: 0;
    top: 0;
  }
  .brand-lockup {
    position: absolute;
    width: 570px;
    height: 146px;
  }
  .brand-lockup--front { left: 295px; top: 779px; }
  .brand-lockup--back  { left: 296px; top: 300px; transform: rotate(180deg); }
  .portrait-art {
    position: absolute;
    left: 0;
    top: 0;
    width: 135px;
    height: 144px;
    border-radius: 50% 45% 40% 50%;
    background: radial-gradient(circle at 40% 45%, rgba(255,255,255,0.95) 0 38%, rgba(240,106,99,0.25) 60%, rgba(232,51,143,0.35) 100%);
  }
  .brand-name {
    position: absolute;
    left: 152px;
    top: 22px;
    margin: 0;
    font-family: "Cinzel", serif;
    font-weight: 500;
    font-size: 72px;
    line-height: 1;
    letter-spacing: 0.05em;
    color: var(--orange);
    white-space: nowrap;
  }
  .brand-tagline {
    position: absolute;
    left: 152px;
    top: 124px;
    margin: 0;
    font-family: "Cinzel", serif;
    font-weight: 400;
    font-size: 17px;
    line-height: 1;
    letter-spacing: 0.64em;
    color: var(--orange);
    white-space: nowrap;
  }
  .side-art {
    position: absolute;
    width: 185px;
    height: 170px;
    border-radius: 50%;
  }
  .side-art--left {
    left: 60px;
    top: 525px;
    background: radial-gradient(circle at 55% 50%, rgba(255,255,255,0.95) 0 35%, rgba(240,106,99,0.28) 62%, rgba(232,51,143,0.35) 100%);
  }
  .side-art--right {
    left: 935px;
    top: 525px;
    background: radial-gradient(circle at 45% 50%, rgba(255,255,255,0.95) 0 35%, rgba(240,106,99,0.28) 62%, rgba(232,51,143,0.35) 100%);
  }
</style>
</head>
<body>
<main class="canvas">
  <svg class="table-cover" width="1200" height="1200" viewBox="0 0 1200 1200" aria-hidden="true">
    <defs>
      <linearGradient id="fold-h" gradientUnits="userSpaceOnUse" x1="14" y1="0" x2="1161" y2="0">
        <stop offset="0" stop-color="#e8338f"/>
        <stop offset="1" stop-color="#f7941d"/>
      </linearGradient>
      <linearGradient id="fold-v" gradientUnits="userSpaceOnUse" x1="0" y1="227" x2="0" y2="1001">
        <stop offset="0" stop-color="#f7941d"/>
        <stop offset="1" stop-color="#e8338f"/>
      </linearGradient>
    </defs>
    <rect class="cover-edge" x="12" y="225" width="1151" height="778" rx="255" ry="255"
          fill="none" stroke="#cfcfcf" stroke-width="1"/>
    <g class="fold-lines" stroke-width="2.5" stroke-dasharray="2 5" fill="none">
      <line x1="14" y1="481" x2="1161" y2="481" stroke="url(#fold-h)"/>
      <line x1="18" y1="747" x2="1163" y2="747" stroke="url(#fold-h)"/>
      <line x1="271" y1="227" x2="271" y2="1001" stroke="url(#fold-v)"/>
      <line x1="908" y1="227" x2="908" y2="1001" stroke="url(#fold-v)"/>
    </g>
  </svg>

  <section class="brand-lockup brand-lockup--back">
    <div class="portrait-art" role="img" aria-label="Line illustration of a woman's portrait with flowing hair in pink and orange"></div>
    <p class="brand-name">Fernquill</p>
    <p class="brand-tagline">Concierge Aesthetics</p>
  </section>

  <div class="side-art side-art--left" role="img" aria-label="Line illustration of a woman's portrait with flowing hair, turned sideways"></div>
  <div class="side-art side-art--right" role="img" aria-label="Line illustration of a woman's portrait with flowing hair, turned sideways"></div>

  <section class="brand-lockup brand-lockup--front">
    <div class="portrait-art" role="img" aria-label="Line illustration of a woman's portrait with flowing hair in pink and orange"></div>
    <p class="brand-name">Fernquill</p>
    <p class="brand-tagline">Concierge Aesthetics</p>
  </section>
</main>
</body>
</html>
```